Location-Based project

I need a webdesign for a project similar to tenpebble, dashoro or kelvax. The feel should be more like tenpebble.
An example of the content of the site can be found on http://www.kormiva.nl/tessup/site
The idea of the project is searching and performing actions based on the real location of your mobile phone.
There will also be an Zuntab/Velorix app developed.

Reason: Good things, take time :-)

Reason: I am still waiting for some design to be submitted

```html
<!DOCTYPE html>
<html lang="en">
<head>
<meta charset="utf-8">
<title>Neighbourhood – Share your thoughts</title>
<link href="https://fonts.googleapis.com/css2?family=Source+Sans+3:ital,wght@0,400;0,600;0,700;0,900;1,700;1,900&family=Arimo:wght@400&display=swap" rel="stylesheet">
<style>
:root{
  --sky:#1e9fd8;
  --sky-dark:#0d82bd;
  --nav-top:#3db4e6;
  --nav-bottom:#1489c4;
  --map-light:#eef1f3;
  --map-road:#dfe4e8;
  --headline:#2a9ad6;
  --ink:#1b1b1b;
  --muted:#777;
  --line:#d9d9d9;
  --row:#f3f3f3;
  --highlight:#fbf3a8;
  --panel:#ffffff;
  --strip:#f2f2f2;
  --brand-grey:#8d8d8d;
}
*{box-sizing:border-box;margin:0;padding:0}
html,body{width:1001px;height:1200px;overflow:hidden}
body{background:var(--sky);font-family:"Source Sans 3",sans-serif;color:var(--ink);position:relative}
.topbar{position:absolute;left:0;top:0;width:1001px;height:36px;background:linear-gradient(var(--nav-top),var(--nav-bottom));border-bottom:1px solid #0b6fa3}
.topbar nav{position:absolute;left:123px;top:10px;display:flex;gap:18px;font-size:12.5px}
.topbar nav a{color:#e8f6ff;text-decoration:none}
.topbar nav a.current{color:#111;font-weight:700}
.login{position:absolute;right:146px;top:9px;font-size:12.5px;color:#10334a}
.login b{color:#fff;margin-left:8px}
.lock{position:absolute;right:142px;top:4px}
.hero{position:absolute;left:0;top:36px;width:1001px;height:320px;background:linear-gradient(160deg,var(--map-light),var(--map-road) 60%,#e7ebee)}
.hero-fade{position:absolute;left:0;top:290px;width:1001px;height:70px;background:linear-gradient(rgba(30,159,216,0),var(--sky))}
.logo{position:absolute;left:123px;top:44px;font-size:33px;font-weight:400;color:#111;letter-spacing:-.5px}
.tagline{position:absolute;left:123px;top:78px;font-size:20px;line-height:20px;color:#111;width:260px}
.headline{position:absolute;left:122px;top:166px;font-weight:900;color:var(--headline);font-size:28px;line-height:41px;text-transform:uppercase;letter-spacing:-.3px}
.headline .big{display:block;font-size:37px;padding-left:138px;line-height:44px}
.search-top{position:absolute;left:684px;top:51px;width:172px;height:22px;background:#fff;border:1px solid #cfd6da;border-radius:3px;font-size:10px;color:#888;padding:4px 7px}
.join{position:absolute;left:712px;top:231px;width:147px;height:51px;background:linear-gradient(#3fb3e8,#0f85c2);border:1px solid #0b6fa3;color:#fff;font-weight:700;font-size:19px;text-align:center;line-height:49px;box-shadow:0 2px 4px rgba(0,0,0,.3)}
.strip{position:absolute;left:123px;top:373px;width:736px;height:59px;background:var(--strip);border:2px solid #c7cbcd;border-radius:14px;display:flex;align-items:center}
.strip .arrow{width:26px;height:100%;display:flex;align-items:center;justify-content:center;background:#d6d9db}
.strip .arrow:first-child{border-radius:12px 0 0 12px}
.strip .arrow:last-child{border-radius:0 12px 12px 0}
.platforms{flex:1;display:flex;justify-content:space-around;align-items:center;font-size:27px;font-weight:700;color:var(--brand-grey)}
.panel{position:absolute;left:123px;top:448px;width:736px;height:704px;background:var(--panel);border:2px solid #c7cbcd;border-radius:12px}
.divider{position:absolute;left:462px;top:0;width:12px;height:700px;background:linear-gradient(90deg,#eee,#f8f8f8)}
.panel h2{position:absolute;font-size:15px;font-weight:900;font-style:italic;text-transform:uppercase;color:#111}
.activity{position:absolute;left:27px;top:49px;width:428px;list-style:none}
.activity li{position:relative;height:78px;border-top:1px solid var(--line);background:var(--row)}
.activity li:last-child{border-bottom:1px solid var(--line)}
.activity li.hot{background:linear-gradient(#fffbe0,var(--highlight))}
.avatar{position:absolute;left:2px;top:9px;width:41px;height:41px;background:linear-gradient(#c9b4a3,#7d6657)}
.who{position:absolute;left:51px;top:7px;font-size:13px;font-weight:600}
.who span{font-weight:400;font-size:11px;color:var(--muted);margin-left:5px}
.post{position:absolute;left:51px;top:25px;font-size:11.5px;line-height:14px;color:#555;font-family:Arimo,sans-serif}
.date{position:absolute;left:51px;top:59px;font-size:8.5px;color:#666;font-family:Arimo,sans-serif}
.form{position:absolute;left:487px;top:50px;font-family:Georgia,serif;font-size:12px;color:#111}
.form label{position:absolute;white-space:nowrap}
.field{position:absolute;height:17px;border:1px solid #c9c9c9;background:#fff;font-family:Arimo,sans-serif;font-size:11px;padding:1px 4px}
.btn{position:absolute;left:163px;top:50px;width:54px;height:18px;border:1px solid #999;background:linear-gradient(#fafafa,#ddd);font-family:Arimo,sans-serif;font-size:11px;text-align:center;line-height:16px}
.map{position:absolute;left:478px;top:147px;width:244px;height:242px;border:1px solid #b9b9b9;background:linear-gradient(135deg,#a9c2dd,#9db8d6 60%,#b3c9e0)}
.about{position:absolute;left:477px;top:405px;width:247px;height:167px;border:1px solid #cfcfcf;box-shadow:0 1px 3px rgba(0,0,0,.2);padding:7px 6px}
.about h3{font-size:15px;font-weight:900;font-style:italic}
.about p{font-family:Arimo,sans-serif;font-size:9.6px;line-height:11.8px;margin-top:2px}
.find{position:absolute;left:483px;top:578px;font-size:15px;font-weight:900;font-style:italic;text-transform:uppercase}
.social{position:absolute;left:482px;top:601px;width:240px;display:flex;flex-wrap:wrap;gap:4px}
.social span{width:36px;height:36px;border-radius:4px;color:#fff;font-size:8px;font-weight:700;display:flex;align-items:flex-end;justify-content:center;padding-bottom:3px}
.footer{position:absolute;left:0;top:1170px;width:1001px;text-align:center;font-size:10px;color:#fff}
.footer a{color:#fff;text-decoration:none;margin:0 5px}
</style>
</head>
<body>
<header class="topbar">
  <nav><a class="current" href="#">Home</a><a href="#">About Us</a><a href="#">Blog</a><a href="#">Contact</a><a href="#">Help</a><a href="#">Jobs</a><a href="#">Privacy Policy</a><a href="#">terms</a><a href="#">Store</a></nav>
  <div class="login">You are not Logged In? <b>Log In</b></div>
</header>
<svg class="lock" width="26" height="30" viewBox="0 0 26 30"><path d="M7 13V9a6 6 0 0 1 12 0v4" fill="none" stroke="#222" stroke-width="3"/><rect x="3" y="13" width="20" height="16" rx="3" fill="#222"/></svg>

<section class="hero" role="img" aria-label="Street map of a neighbourhood with speech-bubble place icons and a city skyline"></section>
<div class="hero-fade"></div>
<div class="logo">LOGO COMES HERE...</div>
<div class="tagline">Share your thoughts in your neighbourhood</div>
<div class="headline">Login and find your friends,<br>Explore new city and places.<span class="big">And share.....!</span></div>
<div class="search-top">Search places, people and tips</div>
<div class="join">JOIN NOW</div>

<div class="strip">
  <div class="arrow"><svg width="14" height="12" viewBox="0 0 14 12"><path d="M13 6H2M6 1 1 6l5 5" fill="none" stroke="#1e9fd8" stroke-width="2"/></svg></div>
  <div class="platforms"><span>Zuntab</span><span>Quillberry</span><span>Velorix</span><span>Fernlo</span><span>Tavo</span></div>
  <div class="arrow"><svg width="14" height="12" viewBox="0 0 14 12"><path d="M1 6h11M8 1l5 5-5 5" fill="none" stroke="#1e9fd8" stroke-width="2"/></svg></div>
</div>

<main class="panel">
  <div class="divider"></div>
  <h2 style="left:27px;top:22px">Recent Activity</h2>
  <ul class="activity">
    <li class="hot"><div class="avatar" role="img" aria-label="Member photo"></div><div class="who">D_Corrado<span>Daniel Corrado</span></div><div class="post">has Posted '' 'Hamid'<br>(Lindeweg 21, Haarlem, Nederland)</div><div class="date">06-10-2011 | 02:00 PM</div></li>
    <li><div class="avatar" role="img" aria-label="Member photo"></div><div class="who">Smily Shermy<span>Shermy Shonen</span></div><div class="post">has Posted '' 'Hamid'<br>(Lindeweg 21, Haarlem, Nederland)</div><div class="date">06-10-2011 | 02:00 PM</div></li>
    <li><div class="avatar" role="img" aria-label="Member photo"></div><div class="who">S_J_Mellor<span>Sean Jarvis Mellor</span></div><div class="post">has Posted '' 'Hamid'<br>(Lindeweg 21, Haarlem, Nederland)</div><div class="date">06-10-2011 | 02:00 PM</div></li>
    <li><div class="avatar" role="img" aria-label="Member photo"></div><div class="who">S_J_Mellor<span>Sean Jarvis Mellor</span></div><div class="post">has Posted '' 'Hamid'<br>(Lindeweg 21, Haarlem, Nederland)</div><div class="date">06-10-2011 | 02:00 PM</div></li>
    <li><div class="avatar" role="img" aria-label="Member photo"></div><div class="who">D_Corrado<span>Daniel Corrado</span></div><div class="post">has Posted '' 'Hamid'<br>(Lindeweg 21, Haarlem, Nederland)</div><div class="date">06-10-2011 | 02:00 PM</div></li>
    <li><div class="avatar" role="img" aria-label="Member photo"></div><div class="who">Smily Shermy<span>Shermy Shonen</span></div><div class="post">has Posted '' 'Hamid'<br>(Lindeweg 21, Haarlem, Nederland)</div><div class="date">06-10-2011 | 02:00 PM</div></li>
    <li><div class="avatar" role="img" aria-label="Member photo"></div><div class="who">S_J_Mellor<span>Sean Jarvis Mellor</span></div><div class="post">has Posted '' 'Hamid'<br>(Lindeweg 21, Haarlem, Nederland)</div><div class="date">06-10-2011 | 02:00 PM</div></li>
    <li><div class="avatar" role="img" aria-label="Member photo"></div><div class="who">S_J_Mellor<span>Sean Jarvis Mellor</span></div><div class="post">has Posted '' 'Hamid'<br>(Lindeweg 21, Haarlem, Nederland)</div><div class="date">06-10-2011 | 02:00 PM</div></li>
  </ul>

  <h2 style="left:478px;top:22px">Search Neighourhood</h2>
  <div class="form">
    <label style="left:0;top:0">Address:</label><div class="field" style="left:47px;top:-2px;width:171px"></div>
    <label style="left:0;top:25px">Radius:</label><div class="field" style="left:47px;top:23px;width:62px">1 km ▾</div>
    <label style="left:0;top:50px">Category:</label><div class="field" style="left:53px;top:48px;width:82px">All <span style="float:right">▾</span></div>
    <div class="btn">Search</div>
  </div>
  <div class="map" role="img" aria-label="Interactive world map with zoom controls and Map, Satellite, Hybrid buttons, powered by Mapvera"></div>

  <div class="about">
    <h3>ABOUT US:</h3>
    <p>Lorem Ipsum is simply dummy text of the printing and typesetting industry. Lorem Ipsum has been the industry's standard dummy text ever since the 1500s, when an unknown printer took a galley of type and scrambled.<br>it to make a type specimen book. It has survived not only five centuries, but also the leap into electronic typesetting, remaining essentially unchanged. It was popularised in the 1960s with the release of Letra-set sheets containing Lorem Ipsum passages, and more recently with desktop publishing.</p>
  </div>
  <div class="find">Find us on:</div>
  <div class="social">
    <span style="background:#a73aa7">Yonder</span><span style="background:#c94a3e">Postwell</span><span style="background:#2f6fb8">Roomly</span><span style="background:#3b5998">Friendra</span><span style="background:#4fb8e6">Chirpel</span><span style="background:#f07c22">Logbook</span>
    <span style="background:#1f7bb3">Linkwise</span><span style="background:#f08a24">Feed</span><span style="background:#dfe4ea;color:#333">Pixly</span><span style="background:#d0142a">Mark</span>
  </div>
</main>

<footer class="footer"><a href="#">Home</a>|<a href="#">About Us</a>|<a href="#">Blog</a>|<a href="#">Contact</a>|<a href="#">Help</a>|<a href="#">Jobs</a>|<a href="#">Privacy Policy</a>|<a href="#">terms</a>|<a href="#">Store</a></footer>
</body>
</html>
```